Peliandro 52

The existing website (peliandro catamaran.com) needs to be simplified.

Need a more restrained style ... lots of white background, fine grey extended titles, a spot of ultramarine or red here and there, one long page for ease of scrolling on a phone.

```html
<!DOCTYPE html>
<html lang="en">
<head>
<meta charset="utf-8">
<title>Peliandro 52 – One Page Website</title>
<link href="https://fonts.googleapis.com/css2?family=Raleway:wght@300;400;500;600;700&family=Open+Sans:wght@400;600&display=swap" rel="stylesheet">
<style>
  :root{
    --page:#ffffff;
    --ultramarine:#1a3cf2;
    --ink:#2d2d2d;
    --title-grey:#8a8a8a;
    --text-grey:#6b6b6b;
    --hairline:#e8e8e8;
    --hero-dark:#0b1a3a;
    --hero-sea:#1d4f8a;
    --workshop-warm:#a08a6a;
    --workshop-light:#d9d2c4;
  }
  *{margin:0;padding:0;box-sizing:border-box}
  html,body{width:1200px;height:2772px;overflow:hidden}
  body{background:var(--page);font-family:"Open Sans",Arial,sans-serif;color:var(--ink);display:flex;flex-direction:column}

  .site-nav{height:72px;flex-shrink:0;display:flex;align-items:center;justify-content:space-between;padding:0 160px;border-bottom:1px solid var(--hairline)}
  .brand{font-family:"Raleway",sans-serif;font-weight:600;font-size:13px;letter-spacing:.22em;text-transform:uppercase;color:var(--ultramarine)}
  .nav-links{display:flex;gap:26px;list-style:none}
  .nav-links li{font-family:"Raleway",sans-serif;font-weight:400;font-size:11px;letter-spacing:.12em;text-transform:uppercase;color:var(--title-grey)}

  main{flex:1;display:flex;flex-direction:column;justify-content:space-evenly;padding:36px 160px 0}

  .hero{position:relative;height:500px;background:linear-gradient(100deg,var(--hero-dark) 0%,#12305e 45%,var(--hero-sea) 100%)}
  .hero-image{position:absolute;inset:0}
  .hero-copy{position:absolute;left:52px;top:150px;width:420px}
  .hero-title{font-family:"Raleway",sans-serif;font-weight:300;font-size:40px;line-height:1.2;letter-spacing:.04em;color:#fff}
  .hero-link{display:inline-block;margin-top:28px;font-family:"Raleway",sans-serif;font-size:11px;font-weight:500;letter-spacing:.2em;text-transform:uppercase;color:#fff;padding-bottom:6px;border-bottom:2px solid var(--ultramarine)}

  .section{display:flex;flex-direction:column;align-items:center;border-top:1px solid var(--hairline);padding-top:56px}
  .section-title{font-family:"Raleway",sans-serif;font-weight:300;font-size:28px;letter-spacing:.3em;text-transform:uppercase;color:var(--title-grey)}
  .title-rule{width:32px;height:2px;background:var(--ultramarine);margin:16px 0 32px}

  .quote{font-family:"Raleway",sans-serif;font-weight:500;font-size:21px;line-height:1.5;text-align:center;color:var(--ink);max-width:700px}
  .quote-mark{color:var(--ultramarine)}
  .quote-author{font-family:"Raleway",sans-serif;font-weight:400;font-size:14px;letter-spacing:.12em;color:var(--title-grey);margin-top:12px}
  .intro{font-size:12px;line-height:1.75;color:var(--text-grey);text-align:center;max-width:620px;margin-top:28px}
  .text-link{margin-top:28px;font-family:"Raleway",sans-serif;font-size:11px;font-weight:600;letter-spacing:.2em;text-transform:uppercase;color:var(--ultramarine);padding-bottom:5px;border-bottom:1px solid var(--ultramarine)}

  .photo{width:760px;height:360px;background:linear-gradient(180deg,var(--workshop-light) 0%,var(--workshop-warm) 55%,#6d5a44 100%)}
  .prose{width:760px;margin-top:32px;display:flex;flex-direction:column;gap:12px}
  .prose p{font-size:12px;line-height:1.75;color:var(--text-grey)}

  .site-footer{height:64px;flex-shrink:0;margin:0 160px;border-top:1px solid var(--hairline);display:flex;align-items:center;justify-content:center;font-size:10px;letter-spacing:.08em;color:var(--title-grey)}
</style>
</head>
<body>

<nav class="site-nav">
  <span class="brand">The Peliandro Catamaran</span>
  <ul class="nav-links"><li>Home</li><li>Hulls</li><li>Wing Mast</li><li>Construction</li><li>Design Aims</li><li>Specifications</li><li>Contact</li></ul>
</nav>

<main>
  <header class="hero">
    <div class="hero-image" role="img" aria-label="Render of a white cruising catamaran with a wing mast sailing on a dark blue sea"></div>
    <div class="hero-copy">
      <h1 class="hero-title">Build A 60-Foot Ocean Cruising Catamaran</h1>
      <span class="hero-link">Discover the Peliandro 52</span>
    </div>
  </header>

  <section class="section section-hulls">
    <h2 class="section-title">Hulls</h2>
    <span class="title-rule"></span>
    <blockquote class="quote"><span class="quote-mark">“</span> Those who fall in love with practice without science are like a sailor who steers a ship without a helm or compass … <span class="quote-mark">”</span></blockquote>
    <p class="quote-author">– Lorenzo Varelli</p>
    <p class="intro">The twin hulls are shaped from a lightweight foam core laminate, designed to slip cleanly through the water while giving a dry, stable and spacious platform for long ocean passages with family and friends aboard.</p>
    <span class="text-link">Read more</span>
  </section>

  <section class="section section-mast">
    <h2 class="section-title">Wing Mast</h2>
    <span class="title-rule"></span>
    <div class="photo" role="img" aria-label="Workshop photo of the long wing mast sections laid out on a timber building jig"></div>
    <div class="prose">
      <p>The rotating wing mast was built in sections and joined together on a long jig set up along the workshop floor.</p>
      <p>Its shape gives the rig more power upwind and lets the boat sail efficiently without a large headsail. The profile was refined over many months of testing.</p>
      <p>Carbon and glass cloth were laid over a foam core, then faired and sanded by hand.</p>
      <p>The mast can be set to feather in strong winds, reducing the load on the rig and making the boat quieter and safer at anchor.</p>
      <p>Each spar section was checked against the design drawings before bonding to the next, keeping the whole mast straight and true along its length.</p>
      <p>Wiring conduits and halyard channels run inside, keeping the mast clean and quiet.</p>
    </div>
  </section>

  <section class="section section-construction">
    <h2 class="section-title">Construction Technique</h2>
    <span class="title-rule"></span>
    <div class="prose">
      <p>The boat is built from foam core panels sheathed in glass and epoxy, a method chosen because it is light, strong and well suited to a small team working in a simple shed without costly moulds or tooling.</p>
      <p>Building a boat at home takes patience and care, but each step is straightforward once the panels are cut and ready.</p>
      <p>Flat panels are laminated on a large table, then bent over temporary frames to form the curved shape of each hull. Seams are taped on both sides and the hull is faired smooth before painting.</p>
      <p>Bulkheads and the bridge deck are fitted once both hulls are turned upright, tying the structure into one stiff platform.</p>
      <p>All joints are bonded with thickened epoxy and reinforced with extra layers of cloth where loads from the rig and rudders are greatest.</p>
      <p>Fit out follows the same approach, with furniture made from the same light panels so the finished boat stays fast and easy to handle.</p>
      <p>Full plans and a building guide explain every stage in detail for anyone wishing to build their own.</p>
    </div>
  </section>
</main>

<footer class="site-footer">Copyright © 2024 Peliandro Catamaran | All Rights Reserved</footer>

</body>
</html>
```